Need Letterhead Design & Matching Business Card

I have a logo that I love already. But the letterhead is less than appealing and boring. I'd like a design for my letterhead which I will match with business cards. Also, I'd like to have used fonts that are generally available, as my current letterhead uses a font named "SPACE" which nobody has unless they download it...so when a Word version is forwarded, it looks awful on the receiver's screed due to not having the font. That being said, modern is the look we like and are going for.

My business is "Halloran Brightmoor PC" - a law firm specializing in representing people who have suffered catastrophic injuries or death (plane, auto, train crashes etc.).

See attached letterhead, which has all of the pertinent information. My logo is also attached in various formats.

```html
<!DOCTYPE html>
<html lang="en">
<head>
<meta charset="utf-8">
<title>Halloran Brightmoor PC — Stationery</title>
<link href="https://fonts.googleapis.com/css2?family=Josefin+Sans:wght@300;400&family=Source+Sans+3:wght@400&display=swap" rel="stylesheet">
<style>
  :root {
    --backdrop: #d3d3d5;
    --paper: #ffffff;
    --ink: #111111;
    --body-grey: #8a8a8e;
    --band: #000000;
  }
  * { margin: 0; padding: 0; box-sizing: border-box; }
  html, body { width: 1194px; height: 1200px; overflow: hidden; }
  body {
    background: var(--backdrop);
    position: relative;
    font-family: "Josefin Sans", sans-serif;
    color: var(--ink);
  }
  .sheet { position: absolute; background: var(--paper); }
  .band { position: absolute; left: 0; right: 0; bottom: 0; background: var(--band); }

  .wordmark {
    position: absolute; left: 0; right: 0;
    display: flex; align-items: center; justify-content: center;
    font-weight: 300; letter-spacing: 0.02em; white-space: nowrap;
    transform: translateY(-50%);
  }
  .wordmark .mark { background: var(--ink); flex: none; }

  /* Letterhead */
  .letterhead { left: 72px; top: 57px; width: 600px; height: 776px; }
  .letterhead .band { height: 24px; }
  .letterhead .wordmark { top: 58px; font-size: 21px; gap: 10px; }
  .letterhead .wordmark .mark { width: 30px; height: 30px; }
  .salutation {
    position: absolute; left: 51px; top: 200px;
    font-family: "Source Sans 3", sans-serif; font-size: 11px; color: var(--body-grey);
  }
  .letter-body {
    position: absolute; left: 39px; top: 249px; width: 523px;
    font-family: "Source Sans 3", sans-serif; font-size: 11px; line-height: 14.1px;
    color: var(--body-grey); text-align: justify;
  }
  .letter-body p + p { margin-top: 14px; }
  .letter-body p:first-child { text-indent: 36px; }

  .contact { position: absolute; font-size: 7px; letter-spacing: 0.08em; text-transform: uppercase; line-height: 1.3; }
  .contact .row { display: flex; align-items: center; gap: 6px; }
  .contact svg { flex: none; }
  .divider { position: absolute; width: 1px; background: var(--ink); }

  .letterhead .addr { left: 37px; top: 716px; }
  .letterhead .divider { left: 300px; top: 702px; height: 43px; }
  .letterhead .links { right: 38px; top: 708px; }

  /* Business cards */
  .card-front { left: 783px; top: 302px; width: 303px; height: 174px; }
  .card-back { left: 789px; top: 527px; width: 302px; height: 173px; }
  .card-front .band, .card-back .band { height: 11px; }
  .card-front .wordmark { top: 47px; font-size: 13px; gap: 6px; }
  .card-back .wordmark { top: 87px; font-size: 14px; gap: 6px; }
  .card-front .wordmark .mark, .card-back .wordmark .mark { width: 22px; height: 22px; }
  .holder { position: absolute; left: 15px; top: 111px; }
  .holder .name { font-size: 9px; letter-spacing: 0.12em; text-transform: uppercase; }
  .holder .role { font-size: 5.5px; letter-spacing: 0.1em; text-transform: uppercase; margin-top: 3px; }
  .card-front .contact { font-size: 4.6px; }
  .card-front .addr { left: 15px; top: 144px; }
  .card-front .divider { left: 153px; top: 134px; height: 24px; }
  .card-front .links { right: 19px; top: 137px; }

  /* Envelope */
  .envelope { left: 66px; top: 884px; width: 634px; height: 283px; }
  .envelope .band { height: 24px; }
  .envelope .wordmark { top: 63px; font-size: 21px; gap: 10px; }
  .envelope .wordmark .mark { width: 30px; height: 30px; }
  .return-address {
    position: absolute; left: 0; right: 0; top: 97px; text-align: center;
    font-size: 7px; letter-spacing: 0.08em; text-transform: uppercase;
  }
</style>
</head>
<body>

<section class="sheet letterhead">
  <div class="wordmark"><span class="mark"></span><span>HALLORAN BRIGHTMOOR PC</span></div>
  <p class="salutation">Dear Sir</p>
  <div class="letter-body">
    <p>Lorem ipsum dolor sit amet, consectetur adipiscing elit. Integer eu odio mattis, pulvinar turpis quis, faucibus nisl. Proin feugiat, erat vitae cursus pharetra, enim est semper ligula, in malesuada orci nisl et diam. Etiam elementum metus ac fringilla vulputate. Etiam mattis ligula sed ante mollis bibendum. Orci varius natoque penatibus et magnis dis parturient montes, nascetur ridiculus mus.</p>
    <p>Ut nibh augue, blandit ac orci ac, rutrum congue enim. Suspendisse gravida vulputate felis, quis interdum orci tincidunt quis. Praesent imperdiet maximus neque. Mauris ut dui enim. Nullam at efficitur elit. Donec ante ipsum, fermentum at lectus vel, blandit vulputate ante. Proin luctus suscipit diam id vestibulum. Morbi malesuada id mauris eget ullamcorper.</p>
    <p>Donec varius orci purus, vitae aliquam libero volutpat id. Integer sed imperdiet libero. Aliquam accumsan, risus sit amet ornare consectetur, turpis felis dictum justo, non rhoncus mauris dui sed velit. Pellentesque habitant morbi tristique senectus et netus et malesuada fames ac turpis egestas. Pellentesque tincidunt vitae ligula nec imperdiet. Donec sed congue enim. Nullam elementum faucibus nulla nec vestibulum. Sed at tempor ligula. In quis vulputate nunc. Integer at gravida lacus, ac tristique risus. Sed at vulputate nulla.</p>
    <p>Praesent blandit nunc eu efficitur commodo. In tempor nisi ex, vel venenatis ante vestibulum a. Duis vestibulum nibh a erat sagittis, nec euismod lorem varius. Nam ultricies turpis sed justo sollicitudin volutpat. Morbi sed mollis eros. Sed quis tortor id enim vehicula porttitor. Curabitur non aliquam ex. Phasellus dignissim fermentum elit, at finibus ligula mattis eget.</p>
  </div>
  <div class="contact addr">
    <div class="row">
      <svg width="8" height="10" viewBox="0 0 8 10"><path d="M4 0a4 4 0 0 0-4 4c0 3 4 6 4 6s4-3 4-6a4 4 0 0 0-4-4zm0 5.5a1.5 1.5 0 1 1 0-3 1.5 1.5 0 0 1 0 3z" fill="#111"/></svg>
      <div>4820 Larkspur Ave. | Suite 600<br>Westfield Hills, CA 90418</div>
    </div>
  </div>
  <div class="divider"></div>
  <div class="contact links">
    <div class="row"><svg width="7" height="6" viewBox="0 0 7 6"><rect x="0.5" y="0.5" width="6" height="5" fill="none" stroke="#111"/><path d="M0.5 0.5l3 2.5 3-2.5" fill="none" stroke="#111"/></svg>talin@halloranbrightmoor.com</div>
    <div class="row"><svg width="7" height="7" viewBox="0 0 7 7"><circle cx="3.5" cy="3.5" r="3" fill="none" stroke="#111"/><path d="M0.5 3.5h6M3.5 0.5v6" stroke="#111" stroke-width="0.7"/></svg>www.halloranbrightmoor.com</div>
    <div class="row"><svg width="7" height="7" viewBox="0 0 7 7"><path d="M1 0.5l1.5 0 .7 1.6-.9.7a4 4 0 0 0 1.9 1.9l.7-.9 1.6.7v1.5c-3.5.3-6-2.2-5.5-5.5z" fill="#111"/></svg>Tel: (855) 555-0142</div>
  </div>
  <div class="band"></div>
</section>

<section class="sheet card-front">
  <div class="wordmark"><span class="mark"></span><span>HALLORAN BRIGHTMOOR PC</span></div>
  <div class="holder">
    <div class="name">R. Talin Vescott</div>
    <div class="role">President</div>
  </div>
  <div class="contact addr">
    <div class="row">
      <svg width="5" height="7" viewBox="0 0 8 10"><path d="M4 0a4 4 0 0 0-4 4c0 3 4 6 4 6s4-3 4-6a4 4 0 0 0-4-4zm0 5.5a1.5 1.5 0 1 1 0-3 1.5 1.5 0 0 1 0 3z" fill="#111"/></svg>
      <div>4820 Larkspur Ave. | Suite 600<br>Westfield Hills, CA 90418</div>
    </div>
  </div>
  <div class="divider"></div>
  <div class="contact links">
    <div class="row"><svg width="4" height="4" viewBox="0 0 7 6"><rect x="0.5" y="0.5" width="6" height="5" fill="#111"/></svg>talin@halloranbrightmoor.com</div>
    <div class="row"><svg width="4" height="4" viewBox="0 0 7 7"><circle cx="3.5" cy="3.5" r="3" fill="none" stroke="#111"/></svg>www.halloranbrightmoor.com</div>
    <div class="row"><svg width="4" height="4" viewBox="0 0 7 7"><path d="M1 0.5l1.5 0 .7 1.6-.9.7a4 4 0 0 0 1.9 1.9l.7-.9 1.6.7v1.5c-3.5.3-6-2.2-5.5-5.5z" fill="#111"/></svg>Tel: (855) 555-0142</div>
  </div>
  <div class="band"></div>
</section>

<section class="sheet card-back">
  <div class="wordmark"><span class="mark"></span><span>HALLORAN BRIGHTMOOR PC</span></div>
  <div class="band"></div>
</section>

<section class="sheet envelope">
  <div class="wordmark"><span class="mark"></span><span>HALLORAN BRIGHTMOOR PC</span></div>
  <p class="return-address">4820 Larkspur Ave. | Suite 600, Westfield Hills, CA 90418</p>
  <div class="band"></div>
</section>

</body>
</html>
```